Create a Professional PowerPoint Slide Deck

I need a professional looking and editable PowerPoint presentation with contents based on the attached PDF.

I would like to see the following;
- add design elements to every slide (cover, title, contents etc)
- enhance the graphs or charts
- same copy will be used
I'm attaching the document to be put into powerpoint (KWRO white paper: "Cargo Wise")

Target Market(s)

Executives and managers responsible for the distribution of products

Industry/Entity Type

It Professional

Font styles to use
Serif

Colors

Designer to choose colors to be used in the design.

Requirements
Must have
• The format should be portrait orientation as this may be printed on paper and converted to PDF for distribution
• Complete conversion of all pages in the attached White Paper
• Upgraded graphics and formatting
Nice to have
• Any creative ideas to make the presentation more attractive or easier to understand
• Color scheme should complement the KWRO Freightlines Logo (red and black)

```html
<!DOCTYPE html>
<html lang="en">
<head>
<meta charset="utf-8">
<title>A Better Way to Handle Multiple Quotes</title>
<link rel="stylesheet" href="https://fonts.googleapis.com/css2?family=Roboto:ital,wght@0,300;0,400;0,700;1,300;1,700&family=Roboto+Condensed:ital,wght@0,700;1,700&display=swap">
<style>
  :root {
    --brand-red: #e8202a;
    --brand-black: #141414;
    --ink: #1e1e1e;
    --paper: #ffffff;
    --canvas: #ffffff;
    --node-blue: #1f6fc1;
    --node-green: #4caf50;
    --caption-red: #f0646a;
    --route-teal: #2a8fa0;
    --route-sand: #d8e4e8;
  }
  * { box-sizing: border-box; margin: 0; padding: 0; }
  html, body { width: 1200px; height: 848px; overflow: hidden; background: var(--canvas); }
  body { position: relative; font-family: "Roboto", Arial, sans-serif; color: var(--ink); }

  .page {
    position: absolute; top: 83px; width: 463px; height: 617px;
    background: var(--paper);
    box-shadow: 3px 4px 7px rgba(0,0,0,.35);
  }
  .page--left { left: 115px; }
  .page--right { left: 635px; }

  .page-header { position: absolute; top: 1px; left: 0; }
  .page-header__kicker {
    display: block; width: 268px; height: 25px; padding: 2px 0 0 29px;
    background: var(--brand-black); color: #fff;
    font: 700 18px/22px "Roboto Condensed", Arial, sans-serif;
    clip-path: polygon(0 0, 100% 0, calc(100% - 18px) 100%, 0 100%);
  }
  .page-header__title {
    display: block; width: 233px; height: 32px; padding: 2px 0 0 29px;
    background: var(--brand-red); color: #fff;
    font: 700 25px/28px "Roboto Condensed", Arial, sans-serif;
    clip-path: polygon(0 0, 100% 0, calc(100% - 22px) 100%, 0 100%);
  }

  .page-body { position: absolute; top: 68px; left: 30px; right: 28px; }
  .section-title {
    color: var(--brand-red);
    font: 700 18px/22px "Roboto Condensed", Arial, sans-serif;
  }
  .section-title--italic { font-style: italic; }
  .copy { font-size: 15.3px; line-height: 19.6px; text-align: justify; }

  .page--left .section-title { margin-bottom: 12px; }
  .page--left .copy { margin-bottom: 15px; }

  .tms-diagram { position: absolute; left: 0; top: 0; width: 463px; height: 617px; }
  .tms-diagram text { font-family: "Roboto", Arial, sans-serif; }
  .figure-caption {
    position: absolute; left: 25px; top: 528px; width: 240px;
    color: var(--caption-red); font: italic 300 12.6px/16px "Roboto", Arial, sans-serif;
  }

  .page--right .page-body { top: 78px; left: 28px; right: 25px; }
  .route-illustration {
    float: right; width: 238px; height: 190px; margin: -45px -14px 6px 8px;
    border-radius: 14px;
    background: linear-gradient(180deg, #cfe6ee 0%, #8fc4d2 30%, #f3d7a1 55%, #a6c76e 75%, var(--route-sand) 100%);
  }
  .page--right .section-title { font-size: 18.5px; line-height: 22px; margin-bottom: 14px; width: 180px; }
  .page--right .copy { font-size: 13px; line-height: 16.8px; }
  .page--right .section-title--wide { width: auto; clear: both; margin-top: 16px; margin-bottom: 10px; }
</style>
</head>
<body>

  <article class="page page--left">
    <header class="page-header">
      <span class="page-header__kicker">A Better Way to Handle</span>
      <span class="page-header__title">Multiple Quotes</span>
    </header>

    <div class="page-body">
      <h2 class="section-title">Beyond the TMS – Using a 3PL</h2>
      <p class="copy">TMS systems are commonly web based and very easy to use. They usually require a monthly fee depending on the number of users and monthly shipments. There may also be a fee for setting up your carriers in the system to get started.</p>
      <h3 class="section-title section-title--italic">What else can you do to improve your logistics system?</h3>
      <p class="copy">If you utilize the services of a 3PL, you will often be able to get a TMS system for no charge as long as you book with their carriers. The 3PL is bringing much more business to the negotiating table than you will alone, so their rates are likely to be lower than yours. So, you get lower rates, spend less time quoting and booking as well as all the other benefits of a TMS while saving money. You also get a single invoice each month covering all of your shipments.</p>
    </div>

    <svg class="tms-diagram" viewBox="0 0 463 617" aria-label="Shipper connects to TMS, which queries multiple carriers">
      <defs>
        <marker id="arrowhead" viewBox="0 0 6 6" refX="5" refY="3" markerWidth="5" markerHeight="5" orient="auto-start-reverse">
          <path d="M0 0 L6 3 L0 6 Z" fill="var(--node-blue)"/>
        </marker>
      </defs>
      <text x="390" y="440" font-size="11" text-anchor="middle" fill="#333">Queries/Quotes</text>
      <text x="322" y="483" font-size="11" text-anchor="middle" fill="#333">Quotes/</text>
      <text x="322" y="496" font-size="11" text-anchor="middle" fill="#333">Booking</text>
      <text x="320" y="576" font-size="11" text-anchor="middle" fill="#333">Historical</text>
      <text x="320" y="589" font-size="11" text-anchor="middle" fill="#333">Data</text>

      <line x1="310" y1="529" x2="330" y2="529" stroke="var(--node-blue)" stroke-width="1.5" marker-start="url(#arrowhead)" marker-end="url(#arrowhead)"/>
      <line x1="367" y1="472" x2="367" y2="496" stroke="var(--node-blue)" stroke-width="1.5" marker-start="url(#arrowhead)" marker-end="url(#arrowhead)"/>
      <line x1="367" y1="563" x2="367" y2="588" stroke="var(--node-blue)" stroke-width="1.5" marker-start="url(#arrowhead)" marker-end="url(#arrowhead)"/>

      <g stroke="var(--node-blue)" stroke-width="1.3" fill="none" marker-end="url(#arrowhead)">
        <path d="M390 452 Q396 456 400 460"/>
        <path d="M410 474 Q418 480 421 487"/>
        <path d="M430 505 Q434 512 434 519"/>
        <path d="M434 541 Q434 549 430 555"/>
        <path d="M421 573 Q416 581 409 586"/>
        <path d="M390 598 Q384 600 377 601"/>
      </g>

      <circle cx="280" cy="529" r="28" fill="var(--node-blue)" stroke="#fff" stroke-width="3"/>
      <circle cx="280" cy="529" r="30" fill="none" stroke="#b9c9dc" stroke-width="1"/>
      <text x="280" y="533" font-size="10" font-weight="700" font-style="italic" text-anchor="middle" fill="#fff">SHIPPER</text>

      <rect x="333" y="503" width="56" height="56" fill="var(--brand-red)"/>
      <text x="361" y="536" font-size="16" font-weight="700" font-style="italic" text-anchor="middle" fill="#fff">TMS</text>

      <g font-size="9" font-weight="700" text-anchor="middle" fill="#fff">
        <circle cx="367" cy="460" r="9.5" fill="var(--node-blue)"/><text x="367" y="463">T</text>
        <circle cx="400" cy="468" r="9.5" fill="var(--node-green)"/><text x="400" y="471">T</text>
        <circle cx="426" cy="495" r="9.5" fill="var(--node-blue)"/><text x="426" y="498">T</text>
        <circle cx="434" cy="530" r="9.5" fill="var(--node-blue)"/><text x="434" y="533">T</text>
        <circle cx="426" cy="565" r="9.5" fill="var(--node-blue)"/><text x="426" y="568">T</text>
        <circle cx="400" cy="592" r="9.5" fill="var(--node-blue)"/><text x="400" y="595">T</text>
        <circle cx="366" cy="601" r="9.5" fill="var(--node-blue)"/><text x="366" y="604">T</text>
      </g>
    </svg>

    <p class="figure-caption">Figure 2. Using a TMS saves time by entering the quote request, receiving multiple quotes assigning the load and printing BOL and Shipping Labels in less than a minute</p>
  </article>

  <article class="page page--right">
    <header class="page-header">
      <span class="page-header__kicker">A Better Way to Handle</span>
      <span class="page-header__title">Multiple Quotes</span>
    </header>

    <div class="page-body">
      <div class="route-illustration" role="img" aria-label="Illustrated winding route from ordering information through ship, rail and warehouse stages to delivered"></div>
      <h2 class="section-title section-title--italic">3PL’s Help You Select the Best Mode at the Best Price</h2>
      <p class="copy">With a 3PL, you also have access to a knowledgeable staff who can help you when your loads might be better served with a partial truckload or full truckload quote. Some 3PL’s provide for putting your carriers in the TMS alongside their carriers and all the carriers bid against each other. If your carrier is selected, you will receive a bill from them and deal directly with them for any service issues. If you use the 3PL’s carriers, you get a combined invoice from the 3PL.</p>
      <h2 class="section-title section-title--italic section-title--wide">Data Stuck In the Cloud Is No Earthly Good</h2>
      <p class="copy">Your logistics system is constantly generating data including pricing by lane, cost per pound, “geographic center of gravity,” and much more. To ignore this information is to lose a great opportunity to understand your system at a deeper level and make informed decisions to improve your performance. Whether it is a big deal like establishing a new distribution center that will result in shorter delivery times at less cost or relatively simple things like combining loads to take advantage of weight breaks, you will benefit greatly from mining the information your system contains.</p>
    </div>
  </article>

</body>
</html>
```